Menu Pared, Maple Lantern

Deseo hacer un menú para pegar en una base de pared del local comercial.
es una heladería pequeña. dimensiones de las bases son de 3m una pared y otra de 3m.
y alto de 45cm aprox.

La imagen adjunta de nombre "example" es un ejemplo de como lo deseo. en cuadros y por categorias.

```html
<!DOCTYPE html>
<html lang="es">
<head>
<meta charset="utf-8">
<title>Maple Lantern — Menú de pared</title>
<link href="https://fonts.googleapis.com/css2?family=Montserrat:wght@400;600;700;800&display=swap" rel="stylesheet">
<style>
  :root{
    --wall:#ececea;
    --frame:#1f1f1f;
    --brand:#5b2a1c;
    --yellow:#f2b01e;
    --orange:#f08a14;
    --orange-light:#f7b54a;
    --panel-light:#f3f3f1;
    --ink:#2a2a2a;
    --ink-soft:#5a5a5a;
    --ink-warm:#4a2a10;
  }
  *{box-sizing:border-box;margin:0;padding:0}
  html,body{width:1200px;height:615px;overflow:hidden}
  body{background:var(--wall);font-family:"Montserrat",sans-serif;color:var(--ink);position:relative}

  .brand-name{position:absolute;left:0;right:0;top:108px;text-align:center;
    font-weight:800;font-size:48px;color:var(--brand);letter-spacing:1px}

  .board{position:absolute;top:263px;height:177px;border:5px solid var(--frame);overflow:hidden}
  .board--granizadas{left:20px;width:284px;background:var(--panel-light)}
  .board--malteadas{left:315px;width:565px;background:linear-gradient(180deg,var(--orange-light),var(--orange))}
  .board--postres{left:891px;width:289px;background:var(--panel-light)}

  .board-header{height:20px;background:var(--yellow);display:flex;align-items:center;justify-content:center;
    font-weight:700;font-size:10px;letter-spacing:1px}
  .board--postres .board-header{justify-content:space-around}

  .photo{position:absolute;border-radius:6px}
  .board--granizadas .photo{left:78px;top:34px;width:125px;height:122px;
    background:radial-gradient(circle at 50% 55%,#d8203a 0 30%,#e8d26a 45%,transparent 70%)}
  .board--malteadas .photo{left:190px;top:22px;width:180px;height:140px;
    background:radial-gradient(ellipse at 50% 55%,#8a4a32 0 30%,#e03040 42%,rgba(255,255,255,.5) 60%,transparent 75%)}
  .board--postres .photo{left:85px;top:38px;width:130px;height:115px;
    background:radial-gradient(ellipse at 50% 55%,#5a2e1c 0 25%,#ffffff 45%,#e4e4e4 65%,transparent 78%)}

  .item{position:absolute;line-height:1.1}
  .item .label{font-size:6px;color:var(--ink-soft)}
  .item .name{font-weight:600;font-size:10px}
  .item .price{font-weight:800;font-size:14px}
  .item .price small{font-size:8px;vertical-align:top}
  .item ul{list-style:none;font-size:6px;line-height:1.3;color:var(--ink-soft);margin-top:3px}
  .board--malteadas .item .label,.board--malteadas .item ul{color:var(--ink-warm)}

  .board-title{position:absolute;left:20px;top:12px;font-weight:800;font-size:14px;letter-spacing:1px}
  .board-brand{position:absolute;right:16px;bottom:10px;font-weight:800;font-size:14px;color:var(--brand)}
</style>
</head>
<body>
  <div class="brand-name">Maple Lantern</div>

  <section class="board board--granizadas">
    <div class="board-header">GRANIZADAS</div>
    <div class="photo" role="img" aria-label="Foto de granizados de fresa, mango y crema en vasos"></div>
    <div class="item" style="left:12px;top:36px">
      <div class="name">Especiales</div>
      <div class="price"><small>$</small>9.200</div>
      <ul><li>Fresa limón</li><li>Mango maracuyá</li></ul>
    </div>
    <div class="item" style="left:212px;top:36px">
      <div class="name">Premium</div>
      <div class="price"><small>$</small>8.400</div>
      <ul><li>Mora</li><li>Fresa crema</li><li>Tropical</li></ul>
    </div>
  </section>

  <section class="board board--malteadas">
    <div class="board-title">MALTEADAS</div>
    <div class="photo" role="img" aria-label="Foto de malteadas con crema, galletas y frutos rojos"></div>
    <div class="item" style="left:20px;top:36px">
      <div class="price"><small>$</small>9.500</div>
      <div class="label">Malteada sencilla</div>
      <div class="name">Simple</div>
    </div>
    <div class="item" style="left:20px;top:80px">
      <div class="label">Malteada</div>
      <div class="name">Medium</div>
      <div class="price"><small>$</small>12.300</div>
    </div>
    <div class="item" style="left:100px;top:92px">
      <ul><li>Vainilla</li><li>Fresa</li></ul>
    </div>
    <div class="item" style="left:20px;top:124px">
      <div class="label">Malteada</div>
      <div class="name">De la casa</div>
      <div class="price"><small>$</small>17.900</div>
    </div>
    <div class="item" style="left:395px;top:22px">
      <div class="label">Malteada</div>
      <div class="name">Especial</div>
      <div class="price"><small>$</small>16.500</div>
      <ul><li>Galleta crema</li><li>Arequipe</li></ul>
    </div>
    <div class="item" style="left:480px;top:14px">
      <div class="label">Malteada</div>
      <div class="name">Licor</div>
      <div class="price"><small>$</small>18.900</div>
      <ul><li>Ron pasas</li><li>Amaretto</li></ul>
    </div>
    <div class="board-brand">Maple Lantern</div>
  </section>

  <section class="board board--postres">
    <div class="board-header"><span>BROWNIE</span><span>HELADOS</span></div>
    <div class="photo" role="img" aria-label="Foto de brownie con helado de vainilla y salsa de chocolate"></div>
    <div class="item" style="left:12px;top:30px">
      <div class="name">Premium</div>
      <div class="price"><small>$</small>4.500</div>
      <ul><li>Con helado</li></ul>
    </div>
    <div class="item" style="left:12px;top:78px">
      <div class="name">Toppings</div>
      <div class="price"><small>$</small>5.700</div>
    </div>
    <div class="item" style="left:12px;top:118px">
      <div class="name">Helado</div>
      <div class="price"><small>$</small>8.800</div>
    </div>
    <div class="item" style="left:225px;top:30px">
      <div class="name">Sencillo</div>
      <div class="price"><small>$</small>3.800</div>
    </div>
    <div class="item" style="left:225px;top:72px">
      <div class="name">Doble</div>
      <div class="price"><small>$</small>6.400</div>
    </div>
  </section>
</body>
</html>
```